e-book cover design "Shore of the whisperwind"
a novel by Trevor K. Hollis
Pm'ed you sir
Draft # 12,
Looks good, just one change I have in mind, the white box that holds "a novel... " should be in a different color, the rest of the cover looks really nice. Good job!
Draft # 10
Its hard to decide between white and blue, both of them look good, I really like this design; good job !
okay sir thanks..
Pixelkidart and designers:
The size for the eBook cover is 600x800 pixels
can i ask what the size of the ebook cover design...so that i can make my design also...thanks

```html
<!DOCTYPE html>
<html lang="en">
<head>
<meta charset="utf-8">
<title>Shore of the Whisperwind — eBook Cover</title>
<link rel="stylesheet" href="https://fonts.googleapis.com/css2?family=Cinzel:wght@700;900&family=Libre+Baskerville:wght@400;700&family=Arimo:wght@400&display=swap">
<style>
  :root {
    --stage-deep: #061a4f;
    --stage-glow: #2fa3e6;
    --stage-mid: #0b3f8f;
    --footer-black: #000000;
    --label-white: #e8eefc;
    --sky-top: #b8360f;
    --sky-upper: #e2661a;
    --sun-gold: #f7c24a;
    --haze-orange: #d9822f;
    --map-dusk: #9a5a3a;
    --city-stone: #c9a982;
    --city-shadow: #7d5a3c;
    --title-brown: #6e2d0c;
    --title-gold: #f2c15a;
    --byline-band: rgba(240, 236, 228, 0.82);
    --byline-ink: #2a1a10;
    --novel-white: #ffffff;
  }
  * { margin: 0; padding: 0; box-sizing: border-box; }
  html, body { width: 1200px; height: 1037px; overflow: hidden; }
  body {
    position: relative;
    background: radial-gradient(ellipse 60% 70% at 50% 70%, var(--stage-glow) 0%, var(--stage-mid) 50%, var(--stage-deep) 100%);
    font-family: "Libre Baskerville", Georgia, serif;
  }
  .size-label {
    position: absolute;
    left: 318px; top: 26px;
    font-family: "Arimo", Arial, sans-serif;
    font-size: 12px;
    letter-spacing: 0.5px;
    color: var(--label-white);
  }
  .footer-band {
    position: absolute;
    left: 0; right: 0; top: 905px; bottom: 0;
    background: var(--footer-black);
  }
  .book-cover {
    position: absolute;
    left: 301px; top: 56px;
    width: 635px; height: 849px;
    overflow: hidden;
    box-shadow: 0 0 24px rgba(0, 0, 0, 0.45);
  }
  .cover-art {
    position: absolute; inset: 0;
    background:
      radial-gradient(circle at 52% 33%, var(--sun-gold) 0%, rgba(247, 194, 74, 0.75) 14%, rgba(226, 102, 26, 0) 34%),
      linear-gradient(to bottom,
        var(--sky-top) 0%,
        var(--sky-upper) 22%,
        var(--haze-orange) 42%,
        var(--map-dusk) 56%,
        var(--city-shadow) 66%,
        var(--city-stone) 80%,
        var(--city-shadow) 100%);
  }
  .title {
    position: absolute;
    left: 0; right: 0; top: 172px;
    text-align: center;
    font-family: "Cinzel", "Times New Roman", serif;
    font-weight: 900;
    color: var(--title-brown);
    text-shadow: 0 0 2px var(--title-gold), 2px 2px 0 var(--title-gold);
    line-height: 1;
  }
  .title-lead { display: block; font-size: 84px; letter-spacing: 2px; }
  .title-joiner { display: block; font-size: 34px; margin-top: 4px; letter-spacing: 1px; }
  .title-tail { display: block; font-size: 50px; margin-top: 2px; letter-spacing: 1px; }
  .novel-label {
    position: absolute;
    left: 0; right: 0; top: 738px;
    text-align: center;
    font-size: 17px;
    color: var(--novel-white);
    text-shadow: 0 1px 2px rgba(0, 0, 0, 0.6);
  }
  .byline-band {
    position: absolute;
    left: 0; right: 0; top: 765px; height: 66px;
    background: var(--byline-band);
    display: flex; align-items: center; justify-content: center;
  }
  .author-name {
    font-size: 29px;
    font-weight: 700;
    color: var(--byline-ink);
    letter-spacing: 0.5px;
  }
</style>
</head>
<body>
  <div class="size-label">600X800 pixels</div>

  <main class="book-cover">
    <div class="cover-art" role="img" aria-label="Sunset sky with a large glowing sun and two fighter jets, a faint regional map overlay, and a sunlit old city skyline with a golden dome below"></div>

    <h1 class="title">
      <span class="title-lead">SHORE</span>
      <span class="title-joiner">OF THE</span>
      <span class="title-tail">WHISPERWIND</span>
    </h1>

    <p class="novel-label">A Novel By</p>
    <div class="byline-band">
      <p class="author-name">Trevor K. Hollis</p>
    </div>
  </main>

  <div class="footer-band"></div>
</body>
</html>
```